New Business Card & Logo Design Project for PR Agency

Halvery & Partners Tech Public Relations agency is looking for a new business card design. Please see our website at www.halvery-pr.example for a description of our services. The design does not necessarily have to match the website’s aesthetic as we are looking for something fresh and modern that reflects our business. We want to emphasize that our focus is on media & public relations, content creation, social media and SEO. We want the business card to convey our BtoB technology focus and should have a very clean look. You are welcome to draw from our current halvery & partners logo on the card or play with that design too. We also like the idea of utilizing blue and white, which are often used in technology-related designs and layouts.
Attached are jpegs of the current logo and current card design for your reference.
Target Market(s)
Our clients are Business-to-Business technology providers.We sell our services to the CEO/President/Marketing director of a technology providing company.
Industry/Entity Type
Business
Look and feel

```html
<!DOCTYPE html>
<html lang="en">
<head>
<meta charset="utf-8">
<title>Halvery &amp; Partners – Business Cards</title>
<link rel="stylesheet" href="https://fonts.googleapis.com/css2?family=Tinos:wght@400;700&family=Open+Sans:wght@400;600&display=swap">
<style>
  :root {
    --bg: #e9e6e1;
    --card: #ffffff;
    --ink: #161616;
    --muted: #555555;
    --accent: #1aa3e0;
    --tab: #111111;
  }
  * { box-sizing: border-box; margin: 0; padding: 0; }
  html, body { width: 1200px; height: 720px; overflow: hidden; }
  body { background: var(--bg); position: relative; font-family: "Open Sans", sans-serif; }

  .card {
    position: absolute; top: 205px;
    width: 540px; height: 309px;
    background: var(--card);
    box-shadow: 0 2px 3px rgba(0,0,0,.12), 0 12px 28px rgba(0,0,0,.14);
    overflow: hidden;
  }
  .card--contact { left: 45px; }
  .card--brand { left: 615px; }

  /* company name set plainly in the card's text face */
  .company-name {
    font-family: "Open Sans", sans-serif; font-weight: 600;
    color: var(--ink); white-space: nowrap; line-height: 1.2;
  }

  /* contact side */
  .card--contact .company-name { position: absolute; left: 38px; top: 42px; font-size: 30px; }
  .holder { position: absolute; right: 40px; top: 112px; text-align: right; }
  .holder__name { font-family: "Tinos", serif; font-weight: 700; font-size: 19px; color: #3a3a3a; }
  .holder__role { font-size: 11px; color: var(--accent); }
  .edge-tab { position: absolute; right: 0; top: 104px; width: 16px; height: 46px; background: var(--tab); border-radius: 10px 0 0 10px; }
  .side-band { position: absolute; left: 0; top: 190px; width: 14px; height: 98px; background: var(--accent); border-radius: 0 8px 8px 0; }

  .contacts { position: absolute; left: 32px; top: 184px; list-style: none; font-size: 13px; color: var(--muted); line-height: 19px; }
  .contacts li { display: flex; align-items: center; gap: 7px; }
  .contacts svg { width: 11px; height: 11px; flex: none; fill: var(--accent); }
  .contacts .address { padding-left: 18px; }

  /* brand side */
  .card--brand .company-name { position: absolute; left: 0; right: 0; top: 102px; text-align: center; font-size: 32px; }
  .tagline { position: absolute; left: 0; right: 0; top: 165px; text-align: center; font-family: "Tinos", serif; font-size: 16px; letter-spacing: 1px; color: var(--ink); }
  .site { position: absolute; left: 0; right: 0; top: 228px; text-align: center; font-size: 17px; letter-spacing: 3px; color: var(--accent); }
</style>
</head>
<body>

<section class="card card--contact" aria-label="Business card, contact side">
  <div class="company-name">halvery &amp; partners</div>
  <div class="edge-tab"></div>
  <div class="holder">
    <div class="holder__name">Daniel Reyes</div>
    <div class="holder__role">Partner</div>
  </div>
  <div class="side-band"></div>
  <ul class="contacts">
    <li><svg viewBox="0 0 12 12" aria-hidden="true"><path d="M2.5 1h2l1 3-1.3 1a6 6 0 0 0 2.8 2.8l1-1.3 3 1v2a1.5 1.5 0 0 1-1.5 1.5A9 9 0 0 1 1 2.5 1.5 1.5 0 0 1 2.5 1z"/></svg>(555) 014-2290</li>
    <li><svg viewBox="0 0 12 12" aria-hidden="true"><rect x="3" y="0.5" width="6" height="11" rx="1.2"/><rect x="4" y="2" width="4" height="6.5" fill="#fff"/></svg>555-014-0789</li>
    <li><svg viewBox="0 0 12 12" aria-hidden="true"><rect x="0.5" y="2" width="11" height="8" rx="1"/><path d="M1 3l5 4 5-4" stroke="#fff" stroke-width="1.2" fill="none"/></svg>dreyes@halvery-pr.example</li>
    <li><svg viewBox="0 0 12 12" aria-hidden="true"><circle cx="6" cy="6" r="5.5"/><path d="M1 6h10M6 .5v11M6 .5c-3 3-3 8 0 11M6 .5c3 3 3 8 0 11" stroke="#fff" stroke-width=".8" fill="none"/></svg>www.halvery-pr.example</li>
    <li class="address">48 Harbor Lane, East Suite 3</li>
    <li class="address">Millbrook, Vermont 05999</li>
  </ul>
</section>

<section class="card card--brand" aria-label="Business card, brand side">
  <div class="company-name">halvery &amp; partners</div>
  <div class="tagline">A PUBLIC RELATION COMPANY</div>
  <div class="site">www.halvery-pr.example</div>
</section>

</body>
</html>
```